refurbishment of diamond cut alloy wheels

we need to design a flyer that will catch the eye of the customer to refurbish diamond cut alloy wheels. we refurbish the wheels by using the latest CNC machine to precision cut and resurface the wheel. we would like before and after pictures of maybe Kelvaron, DXT, Orsa wheels to give it a prestige look. The final design should communicate an expensive look and providing a good image for the business. The colours that I would like to use is black and red which should make the flyer stand out. The logo must sit on a black background without the wordings of specialists in HJ, Orsa etc and also without servicing, diagnostics etc as well. This flyer is just to communicate refurbishment of alloy wheels to high standard.

Target Market(s)

any members of the public and car dealerships

Industry/Entity Type

Automotive

Colors

Designer to choose colors to be used in the design.

Requirements
Must have
• Wow factor with great images of wheels
Nice to have
• Maybe on the front of the flyer it has a picture of a wheel and then on the back of the flyer it has before and after pictures to show how just how incredible it is to refurbish wheels
Should not have
• other makes of wheels apart from DXT, Orsa, and any other high end makes of vehicles wheels

```html
<!DOCTYPE html>
<html lang="en">
<head>
<meta charset="utf-8">
<title>Velden Motors – Wheels &amp; Refurbishments Flyer</title>
<link rel="stylesheet" href="https://fonts.googleapis.com/css2?family=Orbitron:wght@700;900&family=Open+Sans:wght@400;600;700&display=swap">
<style>
  :root{
    --red:#d4202a;
    --red-dark:#8e0f15;
    --black:#0c0c0d;
    --charcoal:#1c1c1f;
    --white:#ffffff;
    --grey:#b9b9bd;
    --stage:#5f6368;
  }
  *{box-sizing:border-box;margin:0;padding:0}
  html,body{width:768px;height:1200px;overflow:hidden}
  body{background:var(--stage);font-family:"Open Sans",Arial,sans-serif;color:var(--white);position:relative}
  .flyer{position:absolute;left:184px;width:400px;height:566px;
    background:radial-gradient(ellipse at 50% 40%,var(--charcoal),var(--black) 75%);
    overflow:hidden;box-shadow:0 6px 20px rgba(0,0,0,.45)}
  .flyer--front{top:17px}
  .flyer--back{top:617px}
  .abs{position:absolute}
  .display{font-family:"Orbitron",Arial,sans-serif;font-weight:900;text-transform:uppercase;line-height:1}

  /* brand */
  .brand{top:20px;left:0;width:100%;display:flex;justify-content:center;align-items:center;gap:8px}
  .brand__mark{width:16px;height:16px;background:var(--red)}
  .brand__name{font-family:"Orbitron",Arial,sans-serif;font-weight:700;font-size:17px;letter-spacing:1px;color:var(--white)}

  /* hero photo */
  .hero{top:62px;left:36px;width:328px;height:176px;border:5px solid var(--grey);border-radius:22px;
    background:linear-gradient(100deg,#c9a63a 0%,#d9b94e 22%,#b4121c 45%,#d0222b 75%,#7d0b11 100%)}

  .headline{top:252px;left:0;width:100%;text-align:center;font-size:46px;color:var(--white);letter-spacing:1px}
  .subhead{top:302px;left:0;width:100%;text-align:center;font-size:26px;color:var(--red)}
  .tagline{top:338px;left:0;width:100%;text-align:center;font-size:11px;font-weight:600;letter-spacing:.4px;text-transform:uppercase}

  .intro{top:364px;left:22px;width:180px;font-size:9px;line-height:1.35}
  .phone-big{top:392px;left:22px;font-family:"Orbitron",Arial,sans-serif;font-weight:700;font-size:21px;color:var(--red)}
  .areas{top:362px;left:214px;width:166px;font-size:8.5px;line-height:1.35;text-align:justify}

  /* contact band */
  .contact{left:0;bottom:0;width:230px;height:92px;background:linear-gradient(180deg,var(--red),var(--red-dark));
    border-top-right-radius:20px;padding:12px 0 0 26px;display:flex;flex-direction:column;gap:6px}
  .contact__row{display:flex;align-items:center;gap:8px;font-size:10.5px;font-weight:700}
  .contact__row svg{width:11px;height:11px;flex:none}

  .address{right:18px;bottom:34px;width:150px;display:flex;gap:8px;align-items:flex-start;font-size:10px;line-height:1.3}
  .address svg{width:12px;height:16px;flex:none;margin-top:2px}
  .rule{right:0;bottom:86px;width:170px;height:3px;background:var(--red)}

  /* back */
  .back-title{top:20px;left:0;width:100%;text-align:center;font-size:15px;color:var(--white)}
  .back-sub{top:40px;left:0;width:100%;text-align:center;font-size:17px;color:var(--red)}
  .shot{width:172px;height:100px;border:3px solid var(--grey);border-radius:8px}
  .shot__label{position:absolute;left:8px;bottom:6px;font-family:"Orbitron",Arial,sans-serif;font-weight:700;font-size:10px;color:var(--white)}
  .shot--before{background:radial-gradient(circle at 45% 55%,#2b2b2e 0 40%,#505056 41% 48%,#c9b12f 70%,#8b8b90 100%)}
  .shot--after{background:radial-gradient(circle at 50% 50%,#e8e8ea 0 12%,#6f7074 30%,#c8c8cc 45%,#2a2a2d 70%,#161618 100%)}
  .shot--before2{background:radial-gradient(circle at 45% 50%,#d9d9dc 0 18%,#222 35%,#505055 55%,#9a9a9f 100%)}
  .shot--after2{background:radial-gradient(circle at 50% 50%,#3a3d44 0 25%,#20232a 50%,#101215 100%)}

  .body-copy{top:292px;left:22px;width:196px;font-size:8px;line-height:1.3;text-align:justify}
  .body-copy p+p{margin-top:5px}
  .makes{top:290px;left:232px;width:150px}
  .makes__title{font-size:11px;color:var(--red);line-height:1.2}
  .makes__list{list-style:none;margin-top:6px;font-size:8px;line-height:1.3;text-transform:uppercase}
  .makes__list li{margin-bottom:3px;padding-left:11px;text-indent:-11px}
  .makes__list li::before{content:"";display:inline-block;width:4px;height:4px;border-radius:50%;background:var(--white);margin-right:7px;vertical-align:middle}
  .cnc{top:424px;left:232px;width:150px;font-size:8px;font-weight:700;line-height:1.3}
</style>
</head>
<body>

<section class="flyer flyer--front">
  <div class="abs brand"><span class="brand__mark"></span><span class="brand__name">VELDEN MOTORS</span></div>
  <div class="abs hero" role="img" aria-label="Photo of a red sports car side-on showing its diamond cut alloy wheel, golden field behind"></div>

  <h1 class="abs display headline">Wheels &amp;</h1>
  <h2 class="abs display subhead">Refurbishments</h2>
  <p class="abs tagline">Refurbishment of alloy wheels to high standard</p>

  <p class="abs intro">If you need premier Alloy Refurbishment services in Slough, please contact us</p>
  <p class="abs phone-big">01632 960 418</p>
  <p class="abs areas">We cater to all locations in and around Colnbrook, Windsor, Hayes, Hounslow, Staines, Ascot and Ashford. For all car body modifications and restorations get in touch with our team of experts today!</p>

  <div class="abs rule"></div>
  <div class="abs address">
    <svg viewBox="0 0 12 16"><path d="M6 0a6 6 0 0 0-6 6c0 4.5 6 10 6 10s6-5.5 6-10a6 6 0 0 0-6-6zm0 8.5A2.5 2.5 0 1 1 6 3.5a2.5 2.5 0 0 1 0 5z" fill="#d4202a"/></svg>
    <span>14B Harrow Lane, Farnley, Berkshire, FN4 2QT</span>
  </div>

  <div class="abs contact">
    <div class="contact__row"><svg viewBox="0 0 12 12"><path d="M2.5 0.5l2 2.5-1.2 1.3a7 7 0 0 0 4.4 4.4L9 7.5l2.5 2-1.5 2C5 11.5.5 7 .5 2z" fill="#fff"/></svg>07700 900 512</div>
    <div class="contact__row"><svg viewBox="0 0 12 12"><circle cx="6" cy="6" r="5" fill="none" stroke="#fff" stroke-width="1.3"/><path d="M1 6h10M6 1c-2.5 3-2.5 7 0 10M6 1c2.5 3 2.5 7 0 10" fill="none" stroke="#fff" stroke-width="1"/></svg>www.veldenmotors.co.uk</div>
    <div class="contact__row"><svg viewBox="0 0 12 12"><rect x="0.5" y="2" width="11" height="8" fill="none" stroke="#fff" stroke-width="1.3"/><path d="M.5 2l5.5 4.5L11.5 2" fill="none" stroke="#fff" stroke-width="1.2"/></svg>info@veldenmotors.co.uk</div>
  </div>
</section>

<section class="flyer flyer--back">
  <h2 class="abs display back-title">Alloy Refurbishment Specialists</h2>
  <h3 class="abs display back-sub">In and around Slough</h3>

  <div class="abs shot shot--before" style="top:70px;left:22px" role="img" aria-label="Before: worn alloy wheel on a yellow car"><span class="shot__label">BEFORE</span></div>
  <div class="abs shot shot--after" style="top:70px;left:206px" role="img" aria-label="After: freshly diamond cut multi-spoke alloy wheel"><span class="shot__label">AFTER</span></div>
  <div class="abs shot shot--before2" style="top:178px;left:22px" role="img" aria-label="Before: scuffed twin-spoke alloy wheel"><span class="shot__label">BEFORE</span></div>
  <div class="abs shot shot--after2" style="top:178px;left:206px" role="img" aria-label="After: refinished dark alloy wheel"><span class="shot__label">AFTER</span></div>

  <div class="abs body-copy">
    <p>If you are looking to refresh the look of your car but don't want the expense of new alloys, with a wide range of limited edition colours to choose from why not consider customising and refurbishing your existing alloys?</p>
    <p>If you've had your alloy wheels long enough for them to require alloy refurbishment you can choose from a wide range of colours for refurbishment or choose a brand new set from our comprehensive range. At Prime Wheels &amp; Tyres, we stock an extensive range of the latest designs from all the leading suppliers and manufacturers so you are sure to find a stylish new design.</p>
  </div>

  <div class="abs makes">
    <h4 class="display makes__title">Cars we specialise in include:</h4>
    <ul class="makes__list">
      <li>Orsa</li>
      <li>Kelvaron</li>
      <li>Sarro</li>
      <li>Kovena</li>
      <li>HJ</li>
      <li>Vehicles of all makes and models</li>
    </ul>
  </div>
  <p class="abs cnc">We refurbish the wheels by using the latest CNC machine to precision cut and resurface the wheel</p>

  <div class="abs rule"></div>
  <div class="abs address">
    <svg viewBox="0 0 12 16"><path d="M6 0a6 6 0 0 0-6 6c0 4.5 6 10 6 10s6-5.5 6-10a6 6 0 0 0-6-6zm0 8.5A2.5 2.5 0 1 1 6 3.5a2.5 2.5 0 0 1 0 5z" fill="#d4202a"/></svg>
    <span>14B Harrow Lane, Farnley, Berkshire, FN4 2QT</span>
  </div>

  <div class="abs contact">
    <div class="contact__row"><svg viewBox="0 0 12 12"><path d="M2.5 0.5l2 2.5-1.2 1.3a7 7 0 0 0 4.4 4.4L9 7.5l2.5 2-1.5 2C5 11.5.5 7 .5 2z" fill="#fff"/></svg>07700 900 512</div>
    <div class="contact__row"><svg viewBox="0 0 12 12"><circle cx="6" cy="6" r="5" fill="none" stroke="#fff" stroke-width="1.3"/><path d="M1 6h10M6 1c-2.5 3-2.5 7 0 10M6 1c2.5 3 2.5 7 0 10" fill="none" stroke="#fff" stroke-width="1"/></svg>www.veldenmotors.co.uk</div>
    <div class="contact__row"><svg viewBox="0 0 12 12"><rect x="0.5" y="2" width="11" height="8" fill="none" stroke="#fff" stroke-width="1.3"/><path d="M.5 2l5.5 4.5L11.5 2" fill="none" stroke="#fff" stroke-width="1.2"/></svg>info@veldenmotors.co.uk</div>
  </div>
</section>

</body>
</html>
```